Maren's Fitness Business Cards

I would like my business cards to look expensive and sophisticated using my logo and the information below.

FRONT
Maren’s Fitness logo

Tag line Grow into your fittest, calmest and most confident self

Maren Holt Pruitt
Personal Trainer

e. maren@marensfitness.example

t. 0781350462

w. www.marensfitness.example

```html
<!DOCTYPE html>
<html lang="en">
<head>
<meta charset="utf-8">
<title>Maren's Fitness Business Cards</title>
<link href="https://fonts.googleapis.com/css2?family=Montserrat:wght@400;500;600&family=Open+Sans:wght@400;600&display=swap" rel="stylesheet">
<style>
  :root {
    --backdrop: #cfcfcf;
    --backdrop-light: #dcdcdc;
    --teal: #6cb3bd;
    --teal-soft: #e4f0f2;
    --mauve: #a3948f;
    --mauve-dark: #8f817c;
    --paper: #ffffff;
    --ink-light: #ffffff;
  }
  * { box-sizing: border-box; margin: 0; padding: 0; }
  html, body { width: 1200px; height: 852px; overflow: hidden; }
  body {
    background: radial-gradient(ellipse at 50% 40%, var(--backdrop-light), var(--backdrop));
    font-family: "Montserrat", "Open Sans", sans-serif;
    position: relative;
  }
  .card {
    position: absolute;
    width: 560px;
    height: 320px;
    border-radius: 22px;
    overflow: hidden;
    box-shadow: 0 6px 18px rgba(0,0,0,0.18);
  }

  /* Front card */
  .card-front {
    left: 90px; top: 80px;
    background: var(--teal);
    color: var(--ink-light);
  }
  .card-front .brand {
    position: absolute;
    left: 0; right: 0; top: 78px;
    display: flex; flex-direction: column; align-items: center; gap: 20px;
  }
  .brand-mark {
    width: 74px; height: 74px;
    border-radius: 50%;
    border: 5px solid currentColor;
  }
  .brand-name {
    font-weight: 400;
    font-size: 24px;
    line-height: 1.25;
    letter-spacing: 8px;
    text-transform: uppercase;
    text-align: center;
  }
  .brand-name span { display: block; }
  .card-front .tagline {
    position: absolute;
    left: 0; right: 0; bottom: 30px;
    text-align: center;
    font-family: "Open Sans", sans-serif;
    font-size: 14px;
    letter-spacing: 0.3px;
  }
  .card-front .faint-circle {
    position: absolute;
    right: -60px; top: -70px;
    width: 300px; height: 300px;
    border-radius: 50%;
    border: 26px solid rgba(255,255,255,0.08);
  }

  /* Back card */
  .card-back {
    left: 550px; top: 452px;
    background: var(--paper);
  }
  .card-back .faint-circle {
    position: absolute;
    left: -40px; top: 40px;
    width: 230px; height: 230px;
    border-radius: 50%;
    border: 20px solid var(--teal-soft);
  }
  .card-back .brand {
    position: absolute;
    right: 34px; top: 22px;
    display: flex; align-items: center; gap: 16px;
    color: var(--teal);
  }
  .card-back .brand-mark { width: 62px; height: 62px; border-width: 4px; }
  .card-back .brand-name { font-size: 20px; letter-spacing: 7px; text-align: left; }
  .divider {
    position: absolute;
    left: 210px; right: 30px; top: 112px;
    height: 1px; background: var(--mauve);
  }
  .person {
    position: absolute;
    left: 40px; top: 128px;
  }
  .person-name {
    color: var(--mauve);
    font-weight: 600;
    font-size: 15px;
    letter-spacing: 1px;
    text-transform: uppercase;
  }
  .person-role {
    color: var(--teal);
    font-weight: 500;
    font-size: 13px;
    letter-spacing: 1px;
    text-transform: uppercase;
    margin-top: 3px;
  }
  .contact {
    position: absolute;
    display: flex; align-items: center; gap: 8px;
    font-family: "Open Sans", sans-serif;
    font-size: 12.5px;
    color: var(--mauve-dark);
  }
  .contact svg { width: 17px; height: 17px; flex: none; }
  .contact-web { right: 34px; top: 124px; }
  .contact-phone { left: 40px; top: 226px; }
  .contact-email { left: 40px; top: 250px; }
  .card-back .band {
    position: absolute; left: 0; bottom: 0;
    width: 560px; height: 40px;
  }
</style>
</head>
<body>

  <section class="card card-front">
    <div class="faint-circle" aria-hidden="true"></div>
    <div class="brand">
      <div class="brand-mark" aria-hidden="true"></div>
      <div class="brand-name"><span>Maren's</span><span>Fitness</span></div>
    </div>
    <p class="tagline">Grow into your fittest, calmest and most confident self</p>
  </section>

  <section class="card card-back">
    <div class="faint-circle" aria-hidden="true"></div>
    <div class="brand">
      <div class="brand-mark" aria-hidden="true"></div>
      <div class="brand-name"><span>Maren's</span><span>Fitness</span></div>
    </div>
    <div class="divider"></div>

    <div class="person">
      <div class="person-name">Maren Holt Pruitt</div>
      <div class="person-role">Personal Trainer</div>
    </div>

    <div class="contact contact-web">
      <svg viewBox="0 0 20 20" aria-hidden="true"><circle cx="10" cy="10" r="10" fill="#6cb3bd"/><circle cx="10" cy="10" r="5.5" fill="none" stroke="#fff" stroke-width="1.2"/><path d="M4.5 10h11M10 4.5c-2.5 3-2.5 8 0 11M10 4.5c2.5 3 2.5 8 0 11" fill="none" stroke="#fff" stroke-width="1"/></svg>
      <span>www.marensfitness.example</span>
    </div>
    <div class="contact contact-phone">
      <svg viewBox="0 0 20 20" aria-hidden="true"><circle cx="10" cy="10" r="10" fill="#6cb3bd"/><path d="M6.5 5.5l2 .2.8 2.2-1.2 1c.6 1.3 1.5 2.2 2.8 2.8l1-1.2 2.2.8.2 2c-.4.7-1.2 1-2 .9-3.4-.6-5.9-3.1-6.5-6.5-.1-.8.2-1.6.7-2.2z" fill="#fff"/></svg>
      <span>0781350462</span>
    </div>
    <div class="contact contact-email">
      <svg viewBox="0 0 20 20" aria-hidden="true"><circle cx="10" cy="10" r="10" fill="#6cb3bd"/><rect x="5" y="6.5" width="10" height="7" rx="1" fill="#fff"/><path d="M5.3 7l4.7 3.6L14.7 7" fill="none" stroke="#6cb3bd" stroke-width="1"/></svg>
      <span>maren@marensfitness.example</span>
    </div>

    <svg class="band" viewBox="0 0 560 40" preserveAspectRatio="none" aria-hidden="true">
      <path d="M0 32 L380 32 L394 14 L560 14 L560 40 L0 40 Z" fill="#a3948f"/>
      <path d="M0 28 L378 28 L392 10 L560 10 L560 14 L394 14 L380 32 L0 32 Z" fill="#6cb3bd"/>
    </svg>
  </section>

</body>
</html>
```